WP website design (Bellwether)

We need a wordpress design for an established auction and real estate company based in Arkansas. The winning design will incorporate a professional color scheme with company logo in a clean layout. The design needs to consider that this will be developed on a responsive theme.

Industry/Entity Type

Real Estate

Font styles to use
Sans Serif

Colors

Designer to choose colors to be used in the design.

Requirements
Must have
• Site will have slideshow, please use stock real estate or other image. A rough idea of homepage content is attached - not necessarily for design purposes.

Navigation Structure is:
1) Home
2) Auctions
3) Services
4) For Sale
5) About Us
6) Reid Videos
7) News & Events
8) Contact Us

Widgets will include:
Social media icons (Social square 1, Social square 2, Social square 3)
Testimonials Widget - this should be prominent
Featured Video
Email Signup form (Sign up to receive exclusive email updates for Bellwether auctions. )
Nice to have
• A drop down menu example
Should not have
• no gavel in the design

```html
<!DOCTYPE html>
<html lang="en">
<head>
<meta charset="utf-8">
<title>Bellwether Auction &amp; Marketing</title>
<link href="https://fonts.googleapis.com/css2?family=Tinos:wght@400;700&family=Arimo:wght@400;700&display=swap" rel="stylesheet">
<style>
:root{
  --green:#0a7a35;
  --green-dark:#05652a;
  --green-light:#1a9a4a;
  --page:#f1f1f1;
  --panel:#ffffff;
  --line:#dedede;
  --text:#6b6b6b;
  --ink:#1e1e1e;
  --footer:#0c1512;
}
*{margin:0;padding:0;box-sizing:border-box}
html,body{width:1200px;height:1059px;overflow:hidden}
body{background:var(--page);font-family:"Tinos","Times New Roman",serif;color:var(--text);position:relative}
.abs{position:absolute}
.brand{left:236px;top:22px;display:flex;align-items:center;gap:8px;color:#2a2a2a}
.brand-dot{width:14px;height:14px;border-radius:50%;background:var(--green)}
.brand-name{font-size:29px;letter-spacing:1px;line-height:1}
.brand-sub{font-size:11.5px;letter-spacing:1px;margin-top:3px;color:var(--green);text-transform:uppercase}
.connect{left:760px;top:31px;text-align:right;width:124px;font-size:10px;color:#777;letter-spacing:.5px}
.connect small{display:block;font-size:8px;letter-spacing:0;margin-top:1px}
.social{top:31px;display:flex;gap:9px;left:900px}
.social span{width:24px;height:24px;background:var(--green);border-radius:3px;display:block}
.nav{left:212px;top:76px;width:776px;height:38px;background:var(--green);border-bottom:2px solid var(--green-dark);display:flex;align-items:center;font-size:10.5px;color:#fff}
.nav a{color:#fff;text-decoration:none;text-align:center}
.nav .home{width:86px;height:38px;line-height:38px;background:var(--green-light);text-decoration:underline;border-right:1px solid var(--green-dark)}
.panel{background:var(--panel);border:1px solid var(--line)}
.slider{left:212px;top:130px;width:518px;height:283px;padding:6px}
.slide{width:100%;height:100%;background:linear-gradient(180deg,#1b2f8a 0%,#3a4ea6 30%,#c9a770 50%,#3e6a2e 72%,#22401a 100%);position:relative}
.dots{position:absolute;left:27px;bottom:16px;display:flex;gap:5px}
.dots i{width:11px;height:11px;border-radius:50%;background:#fff;display:block}
.dots i:first-child{background:var(--green)}
.testi{left:212px;top:421px;width:517px;height:98px;border-left:4px solid var(--green)}
.testi::before{content:"";position:absolute;left:0;top:36px;border:8px solid transparent;border-left-color:var(--green)}
.testi h2{text-align:center;font-weight:400;color:var(--green);font-size:20px;margin-top:6px}
.testi h2 span{color:#bbb;font-size:16px}
.testi p{font-size:9.5px;line-height:12px;margin:8px 20px 0 28px;text-align:justify}
.testi .by{text-align:right;margin-right:92px;color:var(--green);font-size:9.5px}
.tab{left:212px;top:528px;width:193px;height:29px;background:#fff;border:1px solid var(--line);border-bottom:none;color:var(--green);font-size:16px;padding:5px 0 0 12px}
.card{left:212px;width:517px;height:142px}
.card h3{position:absolute;left:16px;top:3px;font-size:19px;font-weight:400;color:var(--ink)}
.card .pic{position:absolute;left:16px;top:36px;width:177px;height:93px;border:1px solid #ccc}
.card .lead{position:absolute;left:203px;top:34px;width:298px;font-size:9.5px;line-height:12px;color:var(--ink);text-align:justify}
.card .body{position:absolute;left:203px;top:70px;width:298px;font-size:9.5px;line-height:12px;text-align:justify}
.more{position:absolute;left:404px;top:112px;width:77px;height:25px;background:var(--green);color:#fff;font-size:10px;text-align:center;line-height:25px;border:1px solid var(--green-dark)}
.about{left:752px;top:130px;width:236px;height:281px}
.about h2{font-size:19px;font-weight:400;color:var(--green);margin:7px 0 0 11px}
.about p{font-size:9.5px;line-height:12px;margin:10px 22px 0 14px;text-align:justify}
.about .portrait{position:absolute;left:40px;top:154px;width:147px;height:127px;background:linear-gradient(180deg,#f4f4f4,#d8c6b0 60%,#a99278)}
.login{left:752px;top:428px;width:236px;height:54px;background:var(--green);border-bottom:2px solid var(--green-dark);color:#fff;font-size:9.5px;font-weight:700}
.field{position:absolute;top:11px;width:72px;height:15px;background:#fff;border:1px solid #9bc;font-size:8px;color:#bbb;padding:1px 8px;font-family:"Arimo",Arial,sans-serif;font-weight:400}
.login svg{position:absolute;top:9px}
.login .lk{position:absolute;top:38px}
.video{left:752px;top:500px;width:236px;height:259px}
.video h2{font-size:19px;font-weight:400;color:var(--green);margin:6px 0 0 11px}
.thumb{position:absolute;width:109px;height:96px;border:1px solid var(--line);padding:4px}
.thumb div{width:100%;height:100%;background:linear-gradient(160deg,#4e6a3c,#8a8a7e 50%,#b33a3a 80%,#6a6a6a);display:flex;align-items:center;justify-content:center}
.thumb svg{display:block}
.video .learn{position:absolute;left:0;width:100%;top:240px;text-align:center;font-size:8px;color:#555}
.phone{left:752px;top:778px;width:236px;height:53px;background:var(--green);border-bottom:2px solid var(--green-dark);color:#fff;font-size:21px;display:flex;align-items:center;padding-left:27px;gap:11px}
.news{left:752px;top:844px;width:236px;height:131px;background:linear-gradient(90deg,#d7d7d7,#f3f3f3 60%,#dcdcdc);border:1px solid #ccc;box-shadow:1px 1px 0 #bbb}
.news h2{font-size:15.5px;font-weight:400;color:#333;margin:17px 0 0 18px}
.news .email{position:absolute;left:15px;top:48px;width:207px;height:28px;background:#fff;border:1px solid #bbb;font-size:10px;color:#aaa;padding:7px 7px}
.news .send{position:absolute;left:17px;top:90px;width:71px;height:25px;background:linear-gradient(#666,#3a3a3a);color:#fff;font-family:"Arimo",Arial,sans-serif;font-weight:700;font-size:11px;text-align:center;line-height:25px;border:1px solid #222}
.footer{left:0;top:1019px;width:1200px;height:40px;background:var(--footer);border-top:3px solid #050a08;color:#cfcfcf;font-size:10px;text-align:center;line-height:38px}
.footer b{color:#e6e6e6}
</style>
</head>
<body>

<div class="abs brand">
  <span class="brand-dot"></span>
  <div><div class="brand-name">BELLWETHER</div><div class="brand-sub">Auction &amp; Marketing, LLC</div></div>
</div>
<div class="abs connect">CONNECT WITH US<small>Post | Comments | E-mail</small></div>
<div class="abs social"><span aria-label="Social profile"></span><span aria-label="Video channel"></span><span aria-label="News feed"></span></div>

<nav class="abs nav">
  <a class="home" href="#">HOME</a>
  <a href="#" style="width:106px">AUCTIONS</a>
  <a href="#" style="width:86px">SERVICES</a>
  <a href="#" style="width:90px">FOR SALE</a>
  <a href="#" style="width:86px">ABOUT US</a>
  <a href="#" style="width:96px">REID VIDEOS</a>
  <a href="#" style="width:106px">NEWS &amp; EVENTS</a>
  <a href="#" style="width:80px">CONTACT US</a>
</nav>

<div class="abs panel slider">
  <div class="slide" role="img" aria-label="Modern luxury home at dusk with lit windows, palm trees and lawn">
    <div class="dots"><i></i><i></i><i></i></div>
  </div>
</div>

<div class="abs panel testi">
  <h2><span>&ldquo;</span> Testimonials <span>&rdquo;</span></h2>
  <p>It has survived not only five centuries, but also the leap into electronic typesetting, remaining essentially unchanged. It was popularised in the 1960s with the release of Letterform sheets containing Lorem Ipsum passages and more recently with desktop publishing software like Pagecraft including versions of Lorem Ipsum.</p>
  <div class="by">-Name</div>
</div>

<div class="abs tab">CURRENT AUCTIONS</div>

<div class="abs panel card" style="top:557px">
  <h3>Real Estate Auction</h3>
  <div class="pic" role="img" aria-label="Green rolling farmland with a red dirt track and marker posts" style="background:linear-gradient(180deg,#c9d6dc,#6f8a6a 35%,#6fb04a 60%,#8a3e26 100%)"></div>
  <p class="lead">It has survived not only five centuries, but also the leap into electronic typesetting, remaining essentially unchanged.</p>
  <p class="body">It was popularised in the 1960s with the release of Letterform sheets containing Lorem Ipsum passages and more recently with desktop publishing software like Pagecraft including versions of Lorem Ipsum.</p>
  <div class="more">MORE &raquo;</div>
</div>

<div class="abs panel card" style="top:708px">
  <h3>Estate Auction</h3>
  <div class="pic" role="img" aria-label="Farm buildings behind a green crop field" style="background:linear-gradient(180deg,#b8c8d8,#d0d4d8 25%,#8a3a3a 38%,#4f8a2a 50%,#3d7a22 100%)"></div>
  <p class="lead">It has survived not only five centuries, but also the leap into electronic typesetting, remaining essentially unchanged.</p>
  <p class="body">It was popularised in the 1960s with the release of Letterform sheets containing Lorem Ipsum passages and more recently with desktop publishing software like Pagecraft including versions of Lorem Ipsum.</p>
  <div class="more">MORE &raquo;</div>
</div>

<div class="abs panel card" style="top:859px">
  <h3>Auction</h3>
  <div class="pic" role="img" aria-label="Blue utility truck parked on grass" style="background:linear-gradient(180deg,#e8eef2,#7a8aa8 35%,#1d3a8a 60%,#4f8a3a 85%,#5f9a40)"></div>
  <p class="lead">It has survived not only five centuries, but also the leap into electronic typesetting, remaining essentially unchanged.</p>
  <p class="body">It was popularised in the 1960s with the release of Letterform sheets containing Lorem Ipsum passages and more recently with desktop publishing software like Pagecraft including versions of Lorem Ipsum.</p>
  <div class="more">MORE &raquo;</div>
</div>

<div class="abs panel about">
  <h2>About Reid Calloway</h2>
  <p>It has survived not only five centuries, but also the leap into electronic typesetting, remaining essentially unchanged.</p>
  <p>It was popularised in the 1960s with the release of Letterform sheets containing Lorem Ipsum passages and more recently with desktop publishing software like Pagecraft including versions of Lorem Ipsum.</p>
  <div class="portrait" role="img" aria-label="Portrait of Reid Calloway in a tan suit"></div>
</div>

<div class="abs login">
  <svg style="left:11px" width="18" height="18" viewBox="0 0 18 18"><circle cx="9" cy="5" r="4" fill="#f2c27a"/><path d="M1 18c0-5 3.5-8 8-8s8 3 8 8z" fill="#e04a2a"/></svg>
  <div class="field" style="left:36px">username</div>
  <svg style="left:122px" width="20" height="20" viewBox="0 0 20 20"><circle cx="14" cy="6" r="5" fill="#f2c23a"/><path d="M11 9L2 18l2 1 1-2 2 1 1-2 1 0 4-5z" fill="#e0a820"/></svg>
  <div class="field" style="left:151px">password</div>
  <span class="lk" style="left:30px">Forgot password?</span>
  <span class="lk" style="left:145px">Create an account</span>
</div>

<div class="abs panel video">
  <h2>Featured Video</h2>
  <div class="thumb" style="left:6px;top:34px"><div role="img" aria-label="Auction crowd outdoors under trees"><svg width="14" height="14" viewBox="0 0 14 14"><path d="M3 1l10 6-10 6z" fill="#fff"/></svg></div></div>
  <div class="thumb" style="left:120px;top:34px"><div role="img" aria-label="Auctioneer in front of a brick house"><svg width="14" height="14" viewBox="0 0 14 14"><path d="M3 1l10 6-10 6z" fill="#fff"/></svg></div></div>
  <div class="thumb" style="left:6px;top:135px"><div role="img" aria-label="Bidders standing on a lawn"><svg width="14" height="14" viewBox="0 0 14 14"><path d="M3 1l10 6-10 6z" fill="#fff"/></svg></div></div>
  <div class="thumb" style="left:120px;top:135px"><div role="img" aria-label="People gathered on a driveway" style="background:linear-gradient(160deg,#cfcfcf,#e8e8e8 50%,#9a9a9a)"><svg width="22" height="22" viewBox="0 0 22 22"><circle cx="11" cy="11" r="11" fill="#111"/><path d="M8 6l8 5-8 5z" fill="#fff"/></svg></div></div>
  <div class="learn">Learn More About Videos Here</div>
</div>

<div class="abs phone">
  <svg width="36" height="36" viewBox="0 0 36 36"><circle cx="18" cy="18" r="16" fill="none" stroke="#fff" stroke-width="2.5"/><path d="M13 9c-2 1-3 3-2 6 2 5 5 9 9 11 3 1 5 0 6-2l-3-3-2 1c-2-1-4-4-5-6l1-2z" fill="#fff"/></svg>
  <span>+123 456 7890</span>
</div>

<div class="abs news">
  <h2>Subscribe to our Newsletter</h2>
  <div class="email">Your email address</div>
  <div class="send">Send</div>
</div>

<footer class="abs footer">&copy; Copyright <b>Bellwether Auction &amp; Marketing.LLC.</b> All Rights Reserved</footer>

</body>
</html>
```